BRIGHTWAVE PARTNERS NAMECARD

Need to design a name card with an existing logo.

As we are professional corporate services provider our name card has to project a professional image.
Should be corporate, simple & professional.

Our corporate color is maroon red but not too dull.

Please refer to our website at www.brightwavepartners.com.sg

Would attach our logo herewith.

Front surface of namecard details:
BRIGHTWAVE PARTNERS PTE LTD
Registration No. 208731945K

Lowe Hui Ting CA (Singapore)
Director

Tel +65 6481 2957
Mobile +65 9172 3806
lowe@brightwavepartners.com.sg
www.brightwavepartners.com.sg

47 Palmer Lane
#07-14 Harbourlight Plaza
Singapore 274153

Back of namecard:-
OUR CORE SERVICES
Incorporation services
Corporate Secretarial Services
Accountancy service
Goods & Services Taxation
Corporate & Personal Taxation
Financial Reporting
Payroll Administration

AFFILIATES:
TRIVANTA CORPORATE SERVICES PTE LTD
BRIGHTWAVEREGISTRYPTE LTD
ORR MANAGEMENT SERVICES PTE LTD
DW LIM AND COMPANY PTE LTD
LEDGERWISE ACADEMY

```html
<!DOCTYPE html>
<html lang="en">
<head>
<meta charset="utf-8">
<title>Brightwave Partners Namecard</title>
<link rel="stylesheet" href="https://fonts.googleapis.com/css2?family=Roboto:wght@400;500;700&family=Roboto+Mono:wght@400;500&display=swap">
<style>
  :root {
    --backdrop: #e6e6e6;
    --brand-red: #d3202f;
    --brand-maroon: #9b111e;
    --paper: #ffffff;
    --ink: #1a1a1a;
    --shadow: rgba(0, 0, 0, 0.18);
  }
  * { box-sizing: border-box; margin: 0; padding: 0; }
  html, body {
    width: 1200px; height: 900px; overflow: hidden;
    background: var(--backdrop);
    font-family: "Roboto", sans-serif;
  }
  .sheet { position: relative; width: 1200px; height: 900px; }

  .card {
    position: absolute; width: 600px; height: 360px;
    box-shadow: 0 6px 18px var(--shadow);
    overflow: hidden;
  }

  /* Back of card */
  .card-back { left: 170px; top: 60px; background: var(--brand-red); color: var(--paper); }
  .card-back .wordmark {
    position: absolute; left: 60px; top: 92px;
    font-weight: 500; font-size: 38px; line-height: 1.05; letter-spacing: 1px;
    text-transform: uppercase;
  }
  .card-back .divider {
    position: absolute; left: 318px; top: 72px; width: 2px; height: 122px;
    background: var(--paper);
  }
  .card-back .services {
    position: absolute; left: 336px; top: 74px; list-style: none;
    font-family: "Roboto Mono", monospace; font-size: 10.5px; line-height: 17px; letter-spacing: 0.4px;
  }
  .card-back .affiliates {
    position: absolute; left: 0; right: 0; top: 258px; text-align: center;
    font-size: 9.5px; line-height: 16px; letter-spacing: 1.2px; text-transform: uppercase;
  }

  /* Front of card */
  .card-front { left: 430px; top: 480px; background: var(--paper); color: var(--ink); }
  .card-front .wordmark {
    position: absolute; right: 40px; top: 38px; text-align: left;
    font-weight: 500; font-size: 30px; line-height: 1.05; letter-spacing: 1px;
    text-transform: uppercase; color: var(--brand-red);
  }
  .card-front .wave { position: absolute; left: 0; top: 0; }
  .contact { position: absolute; left: 40px; top: 92px; }
  .contact .name { font-weight: 700; font-size: 22px; line-height: 26px; }
  .contact .role {
    font-family: "Roboto Mono", monospace; font-size: 11px; line-height: 13px; letter-spacing: 1.5px;
    margin-top: 2px; margin-bottom: 10px;
  }
  .contact .rows { list-style: none; font-family: "Roboto Mono", monospace; font-size: 12px; }
  .contact .rows li { display: flex; align-items: center; height: 20px; }
  .contact .rows svg { width: 13px; height: 13px; margin-right: 12px; flex: none; }
  .contact .address {
    font-family: "Roboto Mono", monospace; font-size: 12px; line-height: 16px;
    margin: 6px 0 0 25px;
  }
  .contact .web {
    font-family: "Roboto Mono", monospace; font-size: 12px; line-height: 16px; letter-spacing: 1px;
    color: var(--brand-red); font-weight: 500; margin: 8px 0 0 25px;
  }
</style>
</head>
<body>
<main class="sheet">

  <section class="card card-back" aria-label="Back of namecard">
    <div class="wordmark">Brightwave<br>Partners</div>
    <div class="divider"></div>
    <ul class="services">
      <li>Incorporation Services</li>
      <li>Corporate Secretarial Services</li>
      <li>Accountancy Services</li>
      <li>Goods &amp; Services Taxation</li>
      <li>Corporate &amp; Personal Taxation</li>
      <li>Financial Reporting</li>
      <li>Payroll Administration</li>
    </ul>
    <p class="affiliates">
      Trivanta Corporate Services Pte Ltd | Brightwaveregistrypte Ltd<br>
      Orr Management Services Pte Ltd | DW Lim and Company Pte Ltd<br>
      Ledgerwise Academy
    </p>
  </section>

  <section class="card card-front" aria-label="Front of namecard">
    <svg class="wave" width="600" height="360" viewBox="0 0 600 360" aria-hidden="true">
      <path d="M0 350 C300 352 460 320 600 170 L600 360 L0 360 Z" fill="var(--brand-maroon)"/>
      <path d="M0 356 C300 357 470 336 600 196 L600 360 L0 360 Z" fill="var(--brand-red)"/>
    </svg>
    <div class="wordmark">Brightwave<br>Partners</div>

    <div class="contact">
      <h1 class="name">Lowe Hui Ting CA</h1>
      <p class="role">DIRECTOR</p>
      <ul class="rows">
        <li>
          <svg viewBox="0 0 13 13" aria-hidden="true"><rect x="3" y="1" width="7" height="11" rx="1" fill="none" stroke="var(--brand-red)" stroke-width="1.6"/></svg>
          +65 9172 3806
        </li>
        <li>
          <svg viewBox="0 0 13 13" aria-hidden="true"><path d="M3 1 L5 4 L4 5.5 C5 7.5 6 8.5 7.5 9 L9 8 L12 10 L10.5 12 C6 12 1 7 1 2.5 Z" fill="var(--brand-red)"/></svg>
          +65 6481 2957
        </li>
        <li>
          <svg viewBox="0 0 13 13" aria-hidden="true"><rect x="3" y="1" width="7" height="4" fill="var(--brand-red)"/><rect x="1" y="5" width="11" height="5" rx="1" fill="var(--brand-red)"/><rect x="3" y="9" width="7" height="3" fill="var(--brand-red)"/></svg>
          +65 6481 2958
        </li>
        <li>
          <svg viewBox="0 0 13 13" aria-hidden="true"><rect x="1" y="3" width="11" height="8" fill="none" stroke="var(--brand-red)" stroke-width="1.4"/><path d="M1 3 L6.5 8 L12 3" fill="none" stroke="var(--brand-red)" stroke-width="1.4"/></svg>
          lowe@brightwavepartners.com.sg
        </li>
      </ul>
      <p class="address">47 Palmer Lane<br>#07-14 Harbourlight Plaza<br>Singapore 274153</p>
      <p class="web">www.brightwavepartners.com.sg</p>
    </div>
  </section>

</main>
</body>
</html>
```